Monthly Newsletter template required for the Irish in London. Read on...

During Summer 2014, a new web site for the Irish in London will launch - www.brolly-hub.com. The purpose of the site is to list all Irish-related activities happening in London inc gigs, sport, arts and culture, business and networks, community, meetups etc.

Each month the database will be sent a monthly e newsletter.
We have linked up with an individual who has been producing a monthly newsletter for some time. The format of his letter is a standard email featuring loads of links and copy. Content rich but with no order or visuals. (copy attached). His newsletter is called 'Barney Quills Weekly' and we're going to stick with the name because it gets people's attention. However, it will be a Brolly-Hub product.

We want the newsletter template to feature an iconic image of Barney, who is the writer of the newsletter. Think of him as a incognito, a spy or a mole. He's mysterious...So, the Barney Quills image for the template needs to reflect this.

The newsletter template design can't be too corporate or too casual as the audience is broad spectrum. It has to be original.

Please note - no shamrocks, leprechauns required though the use of the colour green, in some way, would be good.

Thanks for reading :D

Target Market(s)

The audience main age range is:
Irish
Based in London
Ages: 22 to 45
Crossing over a broad spectrum of occuptations

Industry/Entity Type

Business

Requirements
Must have
• Good content order so that each reader can access their interest areas quickly and easily.
Categories:

Gigs
Sport
Business & Networks
Arts & Culture
Education & General Interest
Community
Charities
Other
Nice to have
• Create a Baarney Quills image that suggests he's mysterious detective. Maybe a silouette of a man in a trench coat and fedora hat? We want the newletter to have a personality.

I've included an image of such a character below. Like the siihouette only and the 'Swift Grey Agent' which could be changed to 'Barney Quills'
Should not have
• Shamrocks or leprechauns

Look and feel must not look too corporate or too casual.

```html
<!DOCTYPE html>
<html lang="en">
<head>
<meta charset="utf-8">
<title>Barney Quills Weekly – July 2014</title>
<link href="https://fonts.googleapis.com/css2?family=Special+Elite&family=Courier+Prime:wght@400;700&display=swap" rel="stylesheet">
<style>
  :root {
    --burlap: #857854;
    --manila: #e4d9bf;
    --manila-edge: #cfc2a2;
    --paper: #f3f0e8;
    --paper-shade: #e6e2d8;
    --ink: #2a2826;
    --ink-soft: #4a4743;
    --stamp-red: #b5372b;
    --note: #f1eee6;
    --clip: #b9bcbf;
    --hub-green: #8ed46f;
  }
  * { box-sizing: border-box; margin: 0; padding: 0; }
  html, body { width: 1200px; height: 3612px; overflow: hidden; }
  body {
    position: relative;
    background:
      repeating-linear-gradient(90deg, rgba(0,0,0,.04) 0 2px, transparent 2px 6px),
      repeating-linear-gradient(0deg, rgba(0,0,0,.04) 0 2px, transparent 2px 6px),
      var(--burlap);
    font-family: "Special Elite", "Courier Prime", monospace;
    color: var(--ink);
  }
  .abs { position: absolute; }
  .nowrap { white-space: nowrap; }

  /* folders and sheets */
  .folder {
    position: absolute;
    background: var(--manila);
    border: 2px solid var(--manila-edge);
    box-shadow: 0 10px 24px rgba(0,0,0,.35);
  }
  .folder-tab {
    position: absolute;
    right: -60px;
    width: 62px; height: 260px;
    background: var(--manila);
    border: 2px solid var(--manila-edge);
    border-left: none;
    border-radius: 0 18px 18px 0;
  }
  .sheet {
    position: absolute;
    background: linear-gradient(160deg, var(--paper), var(--paper-shade));
    box-shadow: 0 4px 10px rgba(0,0,0,.25);
  }

  /* cover */
  .cover-shadow {
    left: 260px; top: 0; width: 660px; height: 880px;
    background: radial-gradient(ellipse at 50% 40%, rgba(70,70,75,.55), rgba(90,90,95,.25) 55%, transparent 75%);
  }
  .stamp {
    left: 140px; top: 170px; width: 500px; height: 170px;
    border: 10px solid var(--stamp-red);
    color: var(--stamp-red);
    font-size: 72px; line-height: 150px; text-align: center;
    white-space: nowrap;
    transform: rotate(-5deg);
    opacity: .88;
  }
  .cover-dateline {
    left: 670px; top: 205px; width: 230px;
    font-size: 20px; text-align: right; line-height: 32px;
    border-top: 2px solid var(--ink-soft); border-bottom: 2px solid var(--ink-soft);
  }
  .masthead { font-variant: small-caps; letter-spacing: 1px; font-weight: 400; }
  .cover-no { left: 560px; top: 520px; width: 340px; text-align: right; font-size: 44px; }
  .cover-title {
    left: 320px; top: 610px; width: 640px; text-align: center;
    font-size: 42px; padding: 8px 0;
    border-top: 2px solid var(--ink-soft); border-bottom: 2px solid var(--ink-soft);
  }
  .cover-url { left: 320px; top: 720px; width: 640px; text-align: center; font-size: 34px; }
  .brand-box {
    left: 200px; top: 820px; width: 460px; height: 240px;
    background: linear-gradient(180deg, #0d1a2a, #1c3f4a 60%, #0f2230);
    display: flex; align-items: center; justify-content: center;
    box-shadow: 0 3px 8px rgba(0,0,0,.4);
  }
  .brand-name { color: var(--hub-green); font-size: 60px; }
  .index-note {
    position: absolute;
    background: var(--note);
    box-shadow: 0 3px 8px rgba(0,0,0,.3);
    font-size: 30px; line-height: 36px; text-align: right;
    padding: 18px 22px;
    white-space: nowrap;
  }
  .note-a { left: 1005px; top: 460px; width: 170px; transform: rotate(1deg); }
  .note-b { left: 665px; top: 760px; width: 355px; transform: rotate(-3deg); }
  .note-c { left: 745px; top: 945px; width: 420px; transform: rotate(1deg); }
  .camera {
    left: 610px; top: 1210px; width: 580px; height: 120px;
    border-radius: 16px;
    background: linear-gradient(180deg, #d9dadb, #8d8f92 55%, #4a4c50);
    box-shadow: 0 8px 16px rgba(0,0,0,.4);
  }
  .clip { position: absolute; }

  /* event pages */
  .photo {
    position: absolute;
    border: 8px solid #fff;
    box-shadow: 0 4px 10px rgba(0,0,0,.4);
    transform: rotate(-6deg);
  }
  .photo-gig { background: radial-gradient(ellipse at 50% 20%, #f0e2c4, #6a4a2e 35%, #141010 75%); }
  .photo-sport { background: linear-gradient(180deg, #3a2418, #c86a2a 55%, #5a2d16); }
  .page-head { position: absolute; left: 620px; width: 360px; text-align: right; }
  .page-head .place { font-size: 17px; }
  .page-head .name { font-size: 42px; line-height: 48px; margin-top: 6px; }
  .page-head .no { font-size: 34px; margin-top: 4px; white-space: nowrap; }
  .page-head .url { font-size: 30px; white-space: nowrap; }
  .section-title { position: absolute; left: 120px; width: 900px; text-align: center; font-size: 38px; line-height: 52px; font-weight: 400; }
  .body-copy { position: absolute; left: 165px; width: 780px; font-size: 21px; line-height: 32px; }
  .body-copy p { margin-bottom: 32px; }
  .read-more { text-align: right; }
  .more-link { position: absolute; left: 120px; width: 900px; text-align: center; font-size: 36px; line-height: 48px; }
  .confidential {
    position: absolute; color: var(--stamp-red);
    font-family: "Courier Prime", monospace; font-weight: 700;
    font-size: 38px; letter-spacing: 2px; transform: rotate(-2deg);
    white-space: nowrap;
  }
</style>
</head>
<body>

<!-- Cover folder -->
<section class="folder" style="left:100px;top:-10px;width:930px;height:1230px;">
  <div class="folder-tab" style="top:940px;"></div>
</section>
<div class="sheet" style="left:130px;top:0;width:860px;height:1200px;"></div>
<div class="abs cover-shadow" role="img" aria-label="Shadow silhouette of Barney Quills in a fedora and trench coat"></div>
<div class="abs stamp">TOP SECRET</div>
<div class="abs cover-dateline">Irish in London<br>July 2014</div>
<div class="abs cover-no nowrap">№ 02345-12</div>
<h1 class="abs cover-title masthead nowrap">Barney Quills Weekly</h1>
<div class="abs cover-url">www.brolly-hub.com</div>
<div class="abs brand-box" role="img" aria-label="Night city skyline with the Brolly-Hub name">
  <span class="brand-name">Brolly-Hub</span>
</div>
<svg class="clip" style="left:110px;top:930px;" width="70" height="150" viewBox="0 0 70 150">
  <path d="M20 140 V25 a15 15 0 0 1 30 0 V120 a10 10 0 0 1 -20 0 V40" fill="none" stroke="var(--clip)" stroke-width="5"/>
</svg>
<nav>
  <div class="index-note note-a">$ Gig<br>$ Sport</div>
  <div class="index-note note-b">$ Business &amp;<br>Networks<br>$ Arts &amp; Culture<br>Community</div>
  <div class="index-note note-c">$ Education &amp;<br>General Interest<br>$ Charities<br>$ Other</div>
</nav>
<div class="abs camera" role="img" aria-label="Miniature spy camera"></div>

<!-- Gig page -->
<section class="folder" style="left:110px;top:1380px;width:930px;height:1440px;">
  <div class="folder-tab" style="top:340px;"></div>
</section>
<div class="sheet" style="left:120px;top:1390px;width:910px;height:1420px;"></div>
<div class="photo photo-gig" style="left:140px;top:1420px;width:440px;height:270px;" role="img" aria-label="Concert crowd with raised hands under stage lights"></div>
<svg class="clip" style="left:170px;top:1385px;" width="60" height="130" viewBox="0 0 60 130">
  <path d="M15 120 V22 a13 13 0 0 1 26 0 V105 a9 9 0 0 1 -18 0 V35" fill="none" stroke="var(--clip)" stroke-width="5"/>
</svg>
<header class="page-head" style="top:1470px;">
  <div class="place">Irish in London</div>
  <div class="name masthead">Barney Quills<br>Weekly</div>
  <div class="no">№ 02345-12</div>
  <div class="url">www.brolly-hub.com</div>
</header>
<h2 class="section-title" style="top:1795px;">Gig events in Londond<br>July 2014</h2>
<div class="body-copy" style="top:1950px;">
  <p>Category brief. Suspendisse commodo suscipit facilisis. Sed gravida nulla sit amet ex lacinia vehicula. Quisque non iaculis diam, quis ornare massa. Maecenas viverra ultrices sodales. Nam congue ornare purus in mattis.</p>
  <p>Do you have memories of nightlife in London? Did you go to clubs or dancehalls? If you have stories to tell about the venue, the music and the dancing, then Islington arts charity Hollyford Arts would like to hear from you.</p>
  <p class="read-more">Read more &gt;&gt;&gt;&gt;</p>
</div>
<div class="more-link" style="top:2470px;">&gt;&gt;&gt; Read more gig events &gt;&gt;&gt;<br>www.brolly-hub.com</div>
<div class="confidential" style="left:680px;top:2610px;">CONFIDENTIAL</div>

<!-- Sport page -->
<section class="folder" style="left:110px;top:2830px;width:930px;height:900px;">
  <div class="folder-tab" style="top:220px;"></div>
</section>
<div class="sheet" style="left:120px;top:2840px;width:910px;height:900px;"></div>
<div class="photo photo-sport" style="left:140px;top:2895px;width:360px;height:235px;" role="img" aria-label="Runner silhouetted against a sunset"></div>
<svg class="clip" style="left:165px;top:2845px;" width="60" height="130" viewBox="0 0 60 130">
  <path d="M15 120 V22 a13 13 0 0 1 26 0 V105 a9 9 0 0 1 -18 0 V35" fill="none" stroke="var(--clip)" stroke-width="5"/>
</svg>
<header class="page-head" style="top:2935px;">
  <div class="place">Irish in London</div>
  <div class="name masthead">Barney Quills<br>Weekly</div>
  <div class="no">№ 02345-12</div>
  <div class="url">www.brolly-hub.com</div>
</header>
<h2 class="section-title" style="top:3245px;">Sport events in Londond<br>July 2014</h2>
<div class="body-copy" style="top:3395px;">
  <p>Category brief. Suspendisse commodo suscipit facilisis. Sed gravida nulla sit amet ex lacinia vehicula. Quisque non iaculis diam, quis ornare massa. Maecenas viverra ultrices sodales. Nam congue ornare purus in mattis.</p>
  <p>The group has arranged a weekend run along the river for Irish clubs.</p>
</div>

</body>
</html>
```